Create a Eye Catching Web Design

We need an informative web design that needs to be eye catching and unique. All of the information needs to be on that page - We have a shopfront setup in the next 2 weeks so the website needs to be ready asap. We are selling mainly rehabilitation aids and mobility products.

The website is main purpose is to inform customers about our range of products, address and phone number. This is an interim website until we get an ecommerce website setup. We are not looking for an ecommerce website, just simple, eye-catching and informative. clean, crisp and modern -target age 45-75 yo (men and women)

I have included our logo and brochure designed with our range of product categories.

The website needs to be designed, coded and setup completely as a finished product.

As soon as the website design is chosen, the chosen designer would need to get the website up and running. If the website design is chosen and great, we could use the same designer for the ecommerce build as well.

www.tolvenacare.com
www.tolvenacare.com.au

Reason: I haven't received as many designs but variations from the same designers.

Target Market(s)

45-75

Industry/Entity Type

Health And Wellness

Coding

Coded - Design and coding required

Number of Pages Required

2 page

Font styles to use
Sans Serif

Requirements
Nice to have
• clean design, modern feel - not cluttered - something unique. for the market age

```html
<!DOCTYPE html>
<html lang="en">
<head>
<meta charset="utf-8">
<title>Tolvena Care – Quality Mobility Products</title>
<link href="https://fonts.googleapis.com/css2?family=Roboto:wght@300;400;500;700&display=swap" rel="stylesheet">
<style>
:root{
  --red:#e31b23;
  --green:#34c70f;
  --cream:#f4eddc;
  --ink:#1d1d1d;
  --text:#666;
  --dark:#1a1a1a;
  --white:#fff;
}
*{box-sizing:border-box;margin:0;padding:0}
html,body{width:1200px;height:4286px;overflow:hidden}
body{font-family:"Roboto",Arial,sans-serif;background:var(--white);color:var(--ink);position:relative}
.abs{position:absolute}

/* header */
.site-header{position:absolute;top:0;left:0;width:1200px;height:108px}
.brand{position:absolute;left:80px;top:30px;display:flex;align-items:center;gap:10px;font-size:34px;font-weight:700;color:var(--red);letter-spacing:1px}
.brand-dot{width:22px;height:22px;border-radius:50%;background:var(--red)}
.contact-top{position:absolute;right:80px;top:14px;font-size:15px;display:flex;gap:26px;color:var(--ink)}
.contact-top span{display:flex;align-items:center;gap:6px}
.contact-top svg{width:14px;height:14px;fill:var(--red)}
.main-nav{position:absolute;right:80px;top:66px;display:flex;gap:18px;font-size:13.5px;text-transform:uppercase}
.main-nav a{color:var(--ink);text-decoration:none}
.main-nav a.active{color:var(--red)}

/* hero */
.hero{position:absolute;top:108px;left:0;width:1200px;height:590px;background:linear-gradient(100deg,#2f5a22 0%,#5f8f3a 35%,#a7c98a 55%,#d6e6c5 70%,#6f9b4a 100%)}
.hero-copy{position:absolute;left:80px;top:150px;width:560px;color:var(--white)}
.hero-copy h1{font-size:40px;font-weight:500;line-height:1.2;text-transform:uppercase}
.hero-copy p{font-size:15.5px;line-height:1.6;margin-top:18px;font-weight:500}
.btn{display:inline-block;border-radius:30px;color:var(--white);font-size:14px;text-transform:uppercase;text-align:center;text-decoration:none}
.btn-red{background:var(--red);padding:14px 32px;margin-top:26px}

/* category strip */
.categories{position:absolute;top:675px;left:80px;width:1040px;display:flex}
.cat{flex:1;height:68px;display:flex;align-items:center;justify-content:center;text-align:center;color:var(--white);font-size:15px;line-height:1.25;text-transform:uppercase;border-right:2px solid var(--white)}
.cat:nth-child(odd){background:var(--red)}
.cat:nth-child(even){background:var(--green)}
.cat-icons{position:absolute;top:743px;left:80px;width:1040px;display:flex}
.cat-icon{flex:1;display:flex;flex-direction:column;align-items:center}
.cat-icon .line{width:2px;height:80px;background:#bbb}
.cat-icon svg{width:86px;height:80px}

/* products */
.section-title{position:absolute;left:0;width:1200px;text-align:center;font-size:30px;font-weight:400;text-transform:uppercase}
.section-title::after{content:"";display:block;width:44px;height:3px;background:var(--red);margin:14px auto 0}
.product{position:absolute;left:80px;width:1040px;height:372px}
.product-frame{position:absolute;top:0;width:330px;height:372px;background:var(--cream);padding:18px}
.product-frame .photo{width:100%;height:100%;border:2px solid var(--red);background:radial-gradient(circle,#fbf8f0 35%,#ded4bf 100%)}
.product-text{position:absolute;top:38px;width:560px}
.product-text h3{font-size:27px;font-weight:400;color:var(--red);text-transform:uppercase}
.product-text p{font-size:14.5px;line-height:1.8;color:var(--text);margin-top:14px}
.product-text p + p{margin-top:8px}
.btn-green{background:var(--green);padding:14px 0;width:176px;margin-top:38px}
.rule{position:absolute;top:52px;height:2px;background:var(--red);width:100px}
.left-img .product-frame{left:0}
.left-img .product-text{left:443px}
.left-img .rule{left:330px}
.right-img .product-frame{right:0}
.right-img .product-text{left:0}
.right-img .rule{right:330px}

/* gallery */
.gallery{position:absolute;top:3591px;left:0;width:1200px;height:258px;display:flex}
.gallery div{flex:1}

/* footer */
.site-footer{position:absolute;top:3914px;left:0;width:1200px;height:315px;background:var(--red);color:var(--white)}
.footer-col{position:absolute;top:70px}
.footer-col h4{font-size:20px;font-weight:500;text-transform:uppercase;padding-bottom:10px;border-bottom:1px solid rgba(255,255,255,.4);margin-bottom:18px}
.footer-col p,.footer-col li{font-size:14px;line-height:1.65}
.footer-col ul{list-style:none}
.info-row{display:flex;align-items:center;gap:14px;margin-bottom:14px;font-size:15px}
.info-row svg{width:16px;height:16px;fill:var(--white)}
.socials{display:flex;gap:10px;margin-top:6px}
.socials span{width:22px;height:22px;border-radius:50%;background:var(--green)}
.bottom-bar{position:absolute;top:4229px;left:0;width:1200px;height:57px;background:var(--dark);color:var(--white);font-size:12px;text-transform:uppercase}
.bottom-bar .copy{position:absolute;left:80px;top:22px}
.pay{position:absolute;right:80px;top:16px;display:flex;align-items:center;gap:8px}
.pay i{width:42px;height:26px;border-radius:3px;background:#ddd;display:block}
</style>
</head>
<body>

<header class="site-header">
  <div class="brand"><span class="brand-dot"></span>TOLVENA CARE</div>
  <div class="contact-top">
    <span><svg viewBox="0 0 24 24"><path d="M6.6 10.8a15.1 15.1 0 006.6 6.6l2.2-2.2c.3-.3.7-.4 1-.2 1.1.4 2.3.6 3.6.6.6 0 1 .4 1 1V20c0 .6-.4 1-1 1A17 17 0 013 4c0-.6.4-1 1-1h3.5c.6 0 1 .4 1 1 0 1.3.2 2.5.6 3.6.1.3 0 .7-.2 1z"/></svg><b>68820415</b></span>
    <span><svg viewBox="0 0 24 24"><path d="M12 2a7 7 0 00-7 7c0 5 7 13 7 13s7-8 7-13a7 7 0 00-7-7zm0 9.5A2.5 2.5 0 1112 6a2.5 2.5 0 010 5.5z"/></svg>14 Kestrel St, Dubbo</span>
  </div>
  <nav class="main-nav">
    <a class="active" href="#">Home</a><a href="#">About Us</a><a href="#">Our Products</a><a href="#">What's New</a><a href="#">Gallery</a><a href="#">Find a Reseller</a><a href="#">Contact Us</a>
  </nav>
</header>

<section class="hero" role="img" aria-label="Smiling carer with an older woman in a wheelchair on a leafy park path">
  <div class="hero-copy">
    <h1>Quality products for<br>a better quality of life.</h1>
    <p>Tolvena Care Offers a Wide Range Of Mobility &amp; Rehab Products Including High End Massage Chairs, Electric Scooters, Wheelchairs, Walkers &amp; Daily Living Aids.</p>
    <a class="btn btn-red" href="#">See our products</a>
  </div>
</section>

<div class="categories">
  <div class="cat">Massage<br>Recliners</div>
  <div class="cat">Electric<br>Scooters</div>
  <div class="cat">Walking<br>Aids</div>
  <div class="cat">Everyday Living<br>Aids</div>
  <div class="cat">Consumer<br>Health</div>
  <div class="cat" style="border-right:0">Wound Care<br>Products</div>
</div>
<div class="cat-icons">
  <div class="cat-icon"><span class="line"></span><svg viewBox="0 0 86 80"><path d="M43 76C10 50 2 36 2 22 2 10 12 2 23 2c9 0 16 5 20 12 4-7 11-12 20-12 11 0 21 8 21 20 0 14-8 28-41 54z" fill="var(--red)"/><circle cx="43" cy="34" r="12" fill="none" stroke="#fff" stroke-width="3"/></svg></div>
  <div class="cat-icon"><span class="line"></span><svg viewBox="0 0 86 80"><path d="M43 76C10 50 2 36 2 22 2 10 12 2 23 2c9 0 16 5 20 12 4-7 11-12 20-12 11 0 21 8 21 20 0 14-8 28-41 54z" fill="var(--green)"/><circle cx="43" cy="34" r="12" fill="none" stroke="#fff" stroke-width="3"/></svg></div>
  <div class="cat-icon"><span class="line"></span><svg viewBox="0 0 86 80"><path d="M43 76C10 50 2 36 2 22 2 10 12 2 23 2c9 0 16 5 20 12 4-7 11-12 20-12 11 0 21 8 21 20 0 14-8 28-41 54z" fill="var(--red)"/><circle cx="43" cy="34" r="12" fill="none" stroke="#fff" stroke-width="3"/></svg></div>
  <div class="cat-icon"><span class="line"></span><svg viewBox="0 0 86 80"><path d="M43 76C10 50 2 36 2 22 2 10 12 2 23 2c9 0 16 5 20 12 4-7 11-12 20-12 11 0 21 8 21 20 0 14-8 28-41 54z" fill="var(--green)"/><circle cx="43" cy="34" r="12" fill="none" stroke="#fff" stroke-width="3"/></svg></div>
  <div class="cat-icon"><span class="line"></span><svg viewBox="0 0 86 80"><path d="M43 76C10 50 2 36 2 22 2 10 12 2 23 2c9 0 16 5 20 12 4-7 11-12 20-12 11 0 21 8 21 20 0 14-8 28-41 54z" fill="var(--red)"/><polyline points="28,36 37,36 41,27 46,43 50,34 58,34" fill="none" stroke="#fff" stroke-width="3"/></svg></div>
  <div class="cat-icon"><span class="line"></span><svg viewBox="0 0 86 80"><path d="M43 76C10 50 2 36 2 22 2 10 12 2 23 2c9 0 16 5 20 12 4-7 11-12 20-12 11 0 21 8 21 20 0 14-8 28-41 54z" fill="var(--green)"/><path d="M39 24h8v8h8v8h-8v8h-8v-8h-8v-8h8z" fill="#fff"/></svg></div>
</div>

<h2 class="section-title" style="top:990px">Our Products</h2>

<article class="product left-img" style="top:1108px">
  <div class="product-frame"><div class="photo" role="img" aria-label="Red and white massage recliner chair"></div></div>
  <span class="rule"></span>
  <div class="product-text">
    <h3>Massgae Recliners</h3>
    <p>Lorem ipsum dolor sit amet, consectetur adipiscing elit. Nunc congue volutpat vestibulum. Cras quis tincidunt eros. Aliquam sodales justo eget pellentesque ullamcorper.</p>
    <p>Nam sit amet diam velit. Duis et metus sit amet turpis vestibulum fermentum malesuada et orci. Integer diam dolor, tincidunt, aliquet nisi.</p>
    <a class="btn btn-green" href="#">View more</a>
  </div>
</article>

<article class="product right-img" style="top:1500px">
  <div class="product-frame"><div class="photo" role="img" aria-label="Covered electric mobility scooter"></div></div>
  <span class="rule"></span>
  <div class="product-text">
    <h3>Electric Scooters</h3>
    <p>Lorem ipsum dolor sit amet, consectetur adipiscing elit. Nunc congue volutpat vestibulum. Cras quis tincidunt eros. Aliquam sodales justo eget pellentesque ullamcorper.</p>
    <p>Nam sit amet diam velit. Duis et metus sit amet turpis vestibulum fermentum malesuada et orci. Integer diam dolor, tincidunt, aliquet nisi.</p>
    <a class="btn btn-green" href="#">View more</a>
  </div>
</article>

<article class="product left-img" style="top:1880px">
  <div class="product-frame"><div class="photo" role="img" aria-label="Folding manual wheelchair"></div></div>
  <span class="rule"></span>
  <div class="product-text">
    <h3>Walking Aids</h3>
    <p>Lorem ipsum dolor sit amet, consectetur adipiscing elit. Nunc congue volutpat vestibulum. Cras quis tincidunt eros. Aliquam sodales justo eget pellentesque ullamcorper.</p>
    <p>Nam sit amet diam velit. Duis et metus sit amet turpis vestibulum fermentum malesuada et orci. Integer diam dolor, tincidunt, aliquet nisi.</p>
    <a class="btn btn-green" href="#">View more</a>
  </div>
</article>

<article class="product right-img" style="top:2270px">
  <div class="product-frame"><div class="photo" role="img" aria-label="Commode chair, walking cane and shower stool"></div></div>
  <span class="rule"></span>
  <div class="product-text">
    <h3>Everyday Living Aids</h3>
    <p>Lorem ipsum dolor sit amet, consectetur adipiscing elit. Nunc congue volutpat vestibulum. Cras quis tincidunt eros. Aliquam sodales justo eget pellentesque ullamcorper.</p>
    <p>Nam sit amet diam velit. Duis et metus sit amet turpis vestibulum fermentum malesuada et orci. Integer diam dolor, tincidunt, aliquet nisi.</p>
    <a class="btn btn-green" href="#">View more</a>
  </div>
</article>

<article class="product left-img" style="top:2650px">
  <div class="product-frame"><div class="photo" role="img" aria-label="Health products: insoles, blood pressure monitor, gel pack and support brace"></div></div>
  <span class="rule"></span>
  <div class="product-text">
    <h3>Consumer Health</h3>
    <p>Lorem ipsum dolor sit amet, consectetur adipiscing elit. Nunc congue volutpat vestibulum. Cras quis tincidunt eros. Aliquam sodales justo eget pellentesque ullamcorper.</p>
    <p>Nam sit amet diam velit. Duis et metus sit amet turpis vestibulum fermentum malesuada et orci. Integer diam dolor, tincidunt, aliquet nisi.</p>
    <a class="btn btn-green" href="#">View more</a>
  </div>
</article>

<article class="product right-img" style="top:3040px">
  <div class="product-frame"><div class="photo" role="img" aria-label="Assorted wound care dressings and bandages"></div></div>
  <span class="rule"></span>
  <div class="product-text">
    <h3>Wound Care Products</h3>
    <p>Lorem ipsum dolor sit amet, consectetur adipiscing elit. Nunc congue volutpat vestibulum. Cras quis tincidunt eros. Aliquam sodales justo eget pellentesque ullamcorper.</p>
    <p>Nam sit amet diam velit. Duis et metus sit amet turpis vestibulum fermentum malesuada et orci. Integer diam dolor, tincidunt, aliquet nisi.</p>
    <a class="btn btn-green" href="#">View more</a>
  </div>
</article>

<h2 class="section-title" style="top:3478px">Our quality products changed peoples' lives</h2>

<div class="gallery">
  <div role="img" aria-label="Wheelchair tennis player on a clay court" style="background:linear-gradient(160deg,#b86a3e,#7d4a2f)"></div>
  <div role="img" aria-label="Older man riding a mobility scooter outdoors" style="background:linear-gradient(160deg,#7c8a6a,#3f4a35)"></div>
  <div role="img" aria-label="Carer with an older woman using a walker" style="background:linear-gradient(160deg,#9fb5c8,#4f6d86)"></div>
  <div role="img" aria-label="Woman relaxing in a massage chair" style="background:linear-gradient(160deg,#4a3c36,#1e1714)"></div>
</div>

<footer class="site-footer">
  <div class="footer-col" style="left:80px;width:290px">
    <h4>Contact Information</h4>
    <div class="info-row"><svg viewBox="0 0 24 24"><path d="M12 2a7 7 0 00-7 7c0 5 7 13 7 13s7-8 7-13a7 7 0 00-7-7zm0 9.5A2.5 2.5 0 1112 6a2.5 2.5 0 010 5.5z"/></svg>14 Kestrel St, Dubbo</div>
    <div class="info-row"><svg viewBox="0 0 24 24"><path d="M6.6 10.8a15.1 15.1 0 006.6 6.6l2.2-2.2c.3-.3.7-.4 1-.2 1.1.4 2.3.6 3.6.6.6 0 1 .4 1 1V20c0 .6-.4 1-1 1A17 17 0 013 4c0-.6.4-1 1-1h3.5c.6 0 1 .4 1 1 0 1.3.2 2.5.6 3.6.1.3 0 .7-.2 1z"/></svg>68820415</div>
    <div class="info-row"><svg viewBox="0 0 24 24"><circle cx="12" cy="12" r="9" fill="none" stroke="#fff" stroke-width="2"/><path d="M3 12h18M12 3c3 3 3 15 0 18M12 3c-3 3-3 15 0 18" fill="none" stroke="#fff" stroke-width="1.5"/></svg>www.tolvenacare.com</div>
    <div class="socials"><span></span><span></span><span></span><span></span></div>
  </div>
  <div class="footer-col" style="left:435px;width:420px">
    <h4>About Us</h4>
    <p>Suspendisse nec ligula eget libero pulvinar pretium. Phasellus arcu dolor, tempus vitae luctus nec, eleifend eu purus.</p>
    <p style="margin-top:12px">Proin dapibus justo lacus, a cursus nisi semper vitae. Sed aliquet augue lorem, nec sollicitudin quam hendrerit eu.</p>
  </div>
  <div class="footer-col" style="left:933px;width:187px">
    <h4>Quick Links</h4>
    <ul><li>Home</li><li>About Us</li><li>Our Products</li><li>What's New</li><li>Gallery</li><li>Find a Reseller</li><li>Contact Us</li></ul>
  </div>
</footer>

<div class="bottom-bar">
  <span class="copy">Copyright@tolvenacare.com. All rights are reserved.</span>
  <div class="pay">We accept: <i></i><i></i><i></i><i></i></div>
</div>

</body>
</html>
```